Velunor
Professional
Martin Calder
Technology Specialist
218 Linden Ave Suite 300
Fairbrook, VA 20391
mcalder@velunor-example.net
www.velunor-example.net
IT Support
Computer Repair
Network Engineering
App Development
Velunor Logo

```html
<!DOCTYPE html>
<html lang="en">
<head>
<meta charset="utf-8">
<title>Velunor Stationery Set</title>
<link rel="stylesheet" href="https://fonts.googleapis.com/css2?family=Montserrat:wght@400;600;700&display=swap">
<style>
  :root {
    --backdrop: #2b2b2b;
    --paper: #ffffff;
    --lime: #9cc83c;
    --lime-soft: #eef5df;
    --slate: #8a8d90;
    --ink: #4a4d50;
    --caption: #8f8f8f;
  }
  * { box-sizing: border-box; margin: 0; padding: 0; }
  html, body { width: 1200px; height: 312px; overflow: hidden; }
  body {
    position: relative;
    background: var(--backdrop);
    font-family: "Montserrat", sans-serif;
    color: var(--ink);
  }
  .sheet { position: absolute; background: var(--paper); overflow: hidden; }
  .band { position: absolute; left: 0; top: 0; bottom: 0; background: var(--lime); }

  .wordmark { position: absolute; display: flex; align-items: center; gap: 4px; }
  .wordmark .dot { width: 6px; height: 6px; border-radius: 50%; background: var(--lime); }
  .wordmark .name { font-weight: 700; letter-spacing: 1px; color: var(--ink); text-transform: uppercase; }
  .wordmark .tagline { position: absolute; left: 10px; top: 100%; font-size: 3px; letter-spacing: 1px; color: var(--slate); text-transform: uppercase; }

  .caption { position: absolute; font-size: 4px; color: var(--caption); text-transform: uppercase; letter-spacing: .5px; }

  /* business cards */
  .card { width: 82px; height: 48px; }
  .card .band { width: 5px; }
  .card .wordmark { left: 14px; top: 15px; }
  .card .name { font-size: 8px; }
  .card-back .details { position: absolute; left: 10px; top: 10px; font-size: 3.2px; line-height: 5px; }
  .card-back .details strong { display: block; font-size: 4.5px; color: var(--ink); }
  .card-back .role { color: var(--lime); }
  .card-back .services { position: absolute; right: 6px; bottom: 7px; font-size: 3px; line-height: 4.5px; text-align: right; color: var(--slate); }

  /* letterheads */
  .letterhead { top: 19px; width: 216px; height: 281px; }
  .letterhead .band { width: 12px; }
  .letterhead .wordmark { left: 28px; top: 36px; }
  .letterhead .name { font-size: 11px; }
  .letterhead .contact { position: absolute; right: 16px; top: 30px; font-size: 3.5px; line-height: 5px; text-align: right; color: var(--slate); }
  .letterhead .backdrop-mark { position: absolute; left: 58px; top: 112px; width: 100px; height: 100px; border-radius: 50%; background: var(--lime-soft); }
  .letterhead .footer-line { position: absolute; left: 28px; right: 16px; bottom: 18px; height: 1px; background: var(--lime-soft); }

  /* envelopes */
  .envelope { left: 684px; width: 216px; height: 110px; }
  .envelope .band { width: 10px; }
  .envelope .wordmark { left: 20px; top: 14px; }
  .envelope .name { font-size: 8px; }
  .envelope .contact { position: absolute; left: 20px; top: 30px; font-size: 3px; line-height: 4.5px; color: var(--slate); }

  .flap-set { position: absolute; left: 919px; width: 257px; }
  .flap-set svg { display: block; }
  .flap-url { position: absolute; left: 0; right: 0; text-align: center; font-size: 5px; letter-spacing: 1px; color: var(--paper); }
</style>
</head>
<body>

  <!-- business cards -->
  <div class="sheet card card-front" style="left:19px; top:113px;">
    <div class="band"></div>
    <div class="wordmark"><span class="dot"></span><span class="name">Velunor</span><span class="tagline">Professional</span></div>
  </div>
  <div class="sheet card card-back" style="left:110px; top:113px;">
    <div class="details">
      <strong>Martin Calder</strong>
      <span class="role">Technology Specialist</span><br>
      218 Linden Ave Suite 300<br>
      Fairbrook, VA 20391<br>
      mcalder@velunor-example.net
    </div>
  </div>
  <div class="sheet card card-front" style="left:19px; top:175px;">
    <div class="band"></div>
    <div class="wordmark"><span class="dot"></span><span class="name">Velunor</span><span class="tagline">Professional</span></div>
  </div>
  <div class="sheet card card-back" style="left:110px; top:175px;">
    <div class="details">
      <strong>Martin Calder</strong>
      <span class="role">Technology Specialist</span><br>
      www.velunor-example.net
    </div>
    <div class="services">IT Support<br>Computer Repair<br>Network Engineering<br>App Development</div>
  </div>

  <!-- letterheads -->
  <div class="sheet letterhead" style="left:221px;">
    <div class="band"></div>
    <div class="wordmark"><span class="dot"></span><span class="name">Velunor</span><span class="tagline">Professional</span></div>
    <div class="contact">218 Linden Ave Suite 300<br>Fairbrook, VA 20391<br>www.velunor-example.net</div>
    <div class="backdrop-mark" role="img" aria-label="Faint brand circle"></div>
    <div class="footer-line"></div>
  </div>
  <div class="caption" style="left:300px; top:303px;">Letterhead one</div>

  <div class="sheet letterhead" style="left:446px;">
    <div class="band"></div>
    <div class="wordmark"><span class="dot"></span><span class="name">Velunor</span><span class="tagline">Professional</span></div>
    <div class="contact">218 Linden Ave Suite 300<br>Fairbrook, VA 20391<br>www.velunor-example.net</div>
    <div class="backdrop-mark" role="img" aria-label="Faint brand circle"></div>
    <div class="footer-line"></div>
  </div>
  <div class="caption" style="left:525px; top:303px;">Letterhead two</div>

  <!-- envelope fronts -->
  <div class="sheet envelope" style="top:24px;">
    <div class="band"></div>
    <div class="wordmark"><span class="dot"></span><span class="name">Velunor</span></div>
    <div class="contact">218 Linden Ave Suite 300<br>Fairbrook, VA 20391</div>
  </div>
  <div class="caption" style="left:768px; top:138px;">Envelope front</div>

  <div class="sheet envelope" style="top:151px;">
    <div class="band"></div>
    <div class="wordmark"><span class="dot"></span><span class="name">Velunor</span></div>
    <div class="contact">218 Linden Ave Suite 300<br>Fairbrook, VA 20391</div>
  </div>
  <div class="caption" style="left:770px; top:268px;">Envelope back</div>

  <!-- envelope backs with flaps -->
  <div class="flap-set" style="top:12px; height:103px;">
    <svg width="257" height="103" viewBox="0 0 257 103">
      <rect x="0" y="0" width="257" height="103" fill="var(--paper)"/>
      <path d="M0 0 H257 V30 Q128 52 0 30 Z" fill="var(--lime)"/>
      <path d="M0 103 L110 58 H147 L257 103 Z" fill="#f2f2f2"/>
    </svg>
    <div class="flap-url" style="top:10px;">www.velunor-example.net</div>
  </div>

  <div class="flap-set" style="top:120px; height:60px;">
    <svg width="257" height="60" viewBox="0 0 257 60">
      <rect x="0" y="0" width="257" height="60" fill="var(--paper)"/>
      <path d="M0 0 H257 V30 Q128 50 0 30 Z" fill="var(--slate)"/>
    </svg>
    <div class="flap-url" style="top:10px;">www.velunor-example.net</div>
  </div>

  <div class="flap-set" style="top:187px; height:113px;">
    <svg width="257" height="113" viewBox="0 0 257 113">
      <path d="M0 40 L128 0 L257 40 Z" fill="#f4f4f4"/>
      <rect x="0" y="40" width="257" height="73" fill="var(--paper)"/>
      <path d="M0 113 L110 72 H147 L257 113 Z" fill="#f2f2f2"/>
    </svg>
    <div class="flap-url" style="top:30px; color:var(--slate);">www.velunor-example.net</div>
  </div>

</body>
</html>
```